Are You Prepared? Know how to support your pre-natal, post-natal and family resilience

I wish to supply a manual (both hardcopy and digit/PDF file/e-booklet) to obstetricians for them to issue to expectant parents. Content will be on pre-natal, post-natal and family mental health tips. I'd like the manual to feel fresh/bright with an educational focus, not mental health stigma, in order to empower prospective parents to up skill and nurture their own resilience and that of their children. Some pages may require me to include content than others. I would also like the option of including illustrations/infographics/diagrams. Please make it compatible with Microsoft Publisher. Thank you for your efforts!!

Target Market(s)

Prospective and expectant parents, young families

Industry/Entity Type

Family Planning

Font styles to use
Serif

Colors

Designer to choose colors to be used in the design.

Requirements
Must have
• • Needed: A booklet template that I can edit content over time, add pages and manipulate the images/text boxes myself.
• • Final deliverables: title page, contents page and several [inner] page layouts that I am able to rotate. Variety in visual layouts so I may repeat combinations to form a manual of 20+ pages.
• • File formats: Microsoft Publisher preferred but PDF files can also be provided (native design files per ArtVantly standards if Publisher not used)
• © Psychologist, Mira Castellude
Nice to have
• Layouts similar to the ones attached
• For designers to gain context for the content, topics will include:
• - Perinatal depression - risk and protective factors
• - Birth process, plan and expectations
• - Realistic expectations to motherhood (recovery, feeding, sleep deprivation, heightened emotions, settling and unsettled baby, bonding, body image, managing priorities, partner dynamics and communication, filtering outside advice and managing family dynamics).
• - Transition of identity. Adjusting to change and fulfillment pendulum.
• Encouraging disclosure
• - Perfectionism, shame and sense of ‘maternal failure’
• - Family dynamics
• - Discipline methods, parent communication, behavioural habits
• - Partner experience - sensitivities, difficulties, support, community attitude, role expectation, bonding, relationship dynamic with partner and extended family.
• - Grandparent boundaries, assistance and transition
• - Medical professionals and perinatal mental health, evidence based info, efficiency
• - Digital screening, mental health first aid skills.
• - Travel
• - Health and special needs
• - Trauma, grief, loss. Miscarriage. Stillborn. Maternal / paternal health. Genetic issues. Fear of mobility and mortality
Should not have
• Mental illness/stigma visuals

```html
<!DOCTYPE html>
<html lang="en">
<head>
<meta charset="utf-8">
<title>Prenatal Examinations – Booklet Spread</title>
<link href="https://fonts.googleapis.com/css2?family=Source+Sans+3:wght@400;600;700&display=swap" rel="stylesheet">
<style>
  :root {
    --canvas: #ffffff;
    --page: #f7f7f7;
    --page-edge: #e2e2e2;
    --ink: #231f20;
    --body-ink: #3a3a3a;
    --rule: #4a4a4a;
    --icon-fill: #e4e6ea;
  }
  * { box-sizing: border-box; margin: 0; padding: 0; }
  html, body {
    width: 1200px; height: 900px; overflow: hidden;
    background: var(--canvas);
    font-family: "Source Sans 3", "Open Sans", sans-serif;
  }
  .spread {
    position: absolute; left: 60px; top: 55px;
    width: 1080px; height: 790px;
    display: flex;
  }
  .page {
    position: relative; width: 540px; height: 790px;
    background: var(--page);
    border: 1px solid var(--page-edge);
  }
  .page--left { border-right: none; }
  .page-title {
    position: absolute; left: 52px; top: 50px;
    font-size: 32px; letter-spacing: -0.3px; color: var(--ink);
    font-weight: 400; line-height: 1;
  }
  .page-title strong { font-weight: 700; }
  .body-copy {
    position: absolute; font-size: 9.6px; line-height: 13px;
    color: var(--body-ink); text-align: justify;
  }
  .body-copy p { margin-bottom: 12px; }
  .body-copy ul { margin: 0 0 12px 14px; }
  .body-copy li { margin-bottom: 1px; }
  .page--left .body-copy { left: 110px; top: 113px; width: 334px; }
  .page--right .body-copy { left: 103px; top: 435px; width: 334px; }

  .exam-item { position: absolute; height: 64px; }
  .exam-icon {
    position: absolute; left: 0; top: 0; width: 64px; height: 64px;
    border: 1px solid var(--rule);
    background: var(--icon-fill);
  }
  .exam-label {
    position: absolute; left: 79px; bottom: 8px; width: 256px;
    font-size: 9.6px; color: var(--body-ink);
    border-bottom: 1px solid var(--rule); padding-bottom: 2px;
  }
  .page--left .exam-item { left: 110px; width: 340px; }
  .page--right .exam-item { left: 99px; width: 340px; }

  .folio {
    position: absolute; bottom: 20px; font-size: 17px; color: var(--ink);
  }
  .page--left .folio { left: 52px; }
  .page--right .folio { right: 52px; }
  .credit {
    position: absolute; bottom: 24px; font-size: 9px; color: var(--body-ink);
  }
  .page--left .credit { right: 12px; }
  .page--right .credit { left: 12px; }
</style>
</head>
<body>
<main class="spread">
  <section class="page page--left">
    <h1 class="page-title"><strong>PRENATAL</strong> EXAMINATIONS</h1>
    <div class="body-copy">
      <p>At the initial antenatal care visit and with the aid of a special booking checklist the pregnant women become classified into either normal risk or high risk.</p>
      <p>In many countries, women are given a summary of their case notes including important background information about their pregnancy for example their medical history, growth charts and any scan reports. If the mother goes to a different hospital for care or to give birth the summary of her case notes can be used by the midwives and doctors until her hospital notes arrive.</p>
      <p>A review looking into women keeping their own case notes shows they have more risk of having a caesarean section. However the women reported feeling more in control having their notes and would like to have them again in future pregnancies. 25% of women reported their hospital notes were lost in hospital though none of the women forgot to take their own notes to any appointments.</p>
      <p>Prenatal diagnosis or prenatal screening (note that "Prenatal Diagnosis" and "Prenatal Screening" refer to two different types of tests) is testing for diseases or conditions in a fetus or embryo before it is born. Obstetricians and midwives have the ability to monitor mother's health and prenatal development during pregnancy through series of regular check-ups.</p>
      <p>Physical examinations generally consist of:</p>
    </div>

    <div class="exam-item" style="top:414px">
      <div class="exam-icon" role="img" aria-label="Line icon for medical history"></div>
      <div class="exam-label">Collection of (mother's) medical history</div>
    </div>

    <div class="exam-item" style="top:496px">
      <div class="exam-icon" role="img" aria-label="Line icon for blood pressure check"></div>
      <div class="exam-label">Checking (mother's) blood pressure</div>
    </div>

    <div class="exam-item" style="top:578px">
      <div class="exam-icon" role="img" aria-label="Line icon for height and weight"></div>
      <div class="exam-label">(Mother's) height and weight</div>
    </div>

    <span class="folio">05</span>
    <span class="credit">© Psychologist, Mira Castellude</span>
  </section>

  <section class="page page--right">
    <div class="exam-item" style="top:112px">
      <div class="exam-icon" role="img" aria-label="Line icon for pelvic exam"></div>
      <div class="exam-label">Pelvic exam</div>
    </div>

    <div class="exam-item" style="top:193px">
      <div class="exam-icon" role="img" aria-label="Line icon for fetal heart rate monitoring"></div>
      <div class="exam-label">Doppler fetal heart rate monitoring</div>
    </div>

    <div class="exam-item" style="top:275px">
      <div class="exam-icon" role="img" aria-label="Line icon for blood and urine tests"></div>
      <div class="exam-label">(Mother's) blood and urine tests</div>
    </div>

    <div class="exam-item" style="top:357px">
      <div class="exam-icon" role="img" aria-label="Line icon for discussion with caregiver"></div>
      <div class="exam-label">Discussion with caregiver</div>
    </div>

    <div class="body-copy">
      <p>In some countries, such as the UK, the symphysial fundal height (SFH) is measured as part of antenatal appointments from 25 weeks gestation. (The SFH is measured from the woman's pubic bone to the top of the uterus). A review into this practice found only one piece of research so there is not enough evidence to say whether measuring the SFH helps to detect small or large babies. As measuring the SFH is not costly and is used in many places, the review recommends carrying on this practice.</p>
      <p>Growth charts are a way of detecting small babies by the measuring the SFH. There are two types of growth chart:</p>
      <ul>
        <li>Population based chart which shows a standard growth and size for each baby</li>
        <li>Customized growth chart which is worked out by looking at the mother's height and weight, and the weights of their previous babies.</li>
      </ul>
      <p>A review looking into which of these charts detected small babies found that there is no good quality research to show which is best. More research is needed before the customized growth charts are recommended because they cost more money and take more time for the health care workers to make.</p>
    </div>

    <span class="credit">© Psychologist, Mira Castellude</span>
    <span class="folio">06</span>
  </section>
</main>
</body>
</html>
```